Concevez un flyer for An event named Celebrate KOLIMBA

Dear All
We are going to organise an event, and we would like to have some flyers and posters.
During this event we will show an African show fashion
- Some African Hair models
- And it is about discovering some African vegetables
Any thoughts, any ideas.
As a designer, you should be able to:
- Think out of the box and produce original designs
Headlines (French):
Maribo Hair Salon & Epicerie Tollane
présente : Celebrating Kolimba, June 20th, 2015
Avec la participation de l'association Aiguilles Solidaires
Headlines (English)
present : Celebrating Kolimba, June 20th, 2015
with the participation of Aiguilles Solidaires
Adresse: Hotel Brimont Lodge
27, rue des Glacinettes
01210 Ferney Voltaire
A partir de 20h (From 8pm)
Come up with nice flyers and posters, and we will work with you on this project. For this project, the budget would be 100 US Dollars.
My thoughts are: An illustration with a black beauty lady, with nice braids and a pot in her hands
Timeline very short (14/04/2015)
Above an example (See attachment)
Flyers sizing A5 (5.83 inchesx8.27 inches) - Front and back.
Posters (23.39 inches x 33.11 inches

```html
<!DOCTYPE html>
<html lang="fr">
<head>
<meta charset="utf-8">
<title>Celebrating Kolimba 2015 – Flyer</title>
<link rel="stylesheet" href="https://fonts.googleapis.com/css2?family=Black+Ops+One&family=Bree+Serif&family=Dancing+Script:wght@600&family=Open+Sans:ital,wght@0,600;0,700;1,600&family=PT+Serif:wght@700&display=swap">
<style>
  :root {
    --sky-top: #3f4c54;
    --sky-mid: #8e9a98;
    --sky-light: #c9c3a8;
    --sunset: #e8953a;
    --sunset-deep: #c8641c;
    --ground: #1b130d;
    --portrait-light: #c4772e;
    --portrait-mid: #7a3f1c;
    --portrait-dark: #3b1d0e;
    --host-yellow: #f6d43c;
    --host-outline: #2a2418;
    --title-green: #2c4628;
    --script-dark: #23301f;
    --badge-orange: #ef8a1f;
    --badge-ring: #fff6e6;
    --badge-text: #3a1c0a;
    --address-ink: #1f1a14;
    --price-red: #7b1f0f;
    --white: #ffffff;
  }
  * { margin: 0; padding: 0; box-sizing: border-box; }
  html, body { width: 854px; height: 1200px; overflow: hidden; background: var(--ground); }
  .flyer {
    position: relative;
    width: 854px;
    height: 1200px;
    overflow: hidden;
  }
  .scene {
    position: absolute;
    inset: 0;
    background:
      radial-gradient(ellipse 520px 360px at 330px 760px, rgba(232,149,58,0.55), transparent 70%),
      linear-gradient(180deg,
        var(--sky-top) 0%,
        var(--sky-mid) 28%,
        var(--sky-light) 48%,
        var(--sunset) 64%,
        var(--sunset-deep) 72%,
        var(--ground) 76%,
        var(--ground) 100%);
  }
  .portrait {
    position: absolute;
    left: 50px;
    top: 360px;
    width: 470px;
    height: 840px;
    border-radius: 190px 190px 40px 40px;
    background: linear-gradient(180deg,
      var(--portrait-dark) 0%,
      var(--portrait-mid) 30%,
      var(--portrait-light) 55%,
      var(--portrait-mid) 78%,
      var(--portrait-dark) 100%);
  }
  .hosts {
    position: absolute;
    top: 8px;
    left: 0;
    width: 100%;
    text-align: center;
    font-family: "Bree Serif", serif;
    color: var(--host-yellow);
    font-size: 31px;
    line-height: 58px;
    text-shadow: -2px -2px 0 var(--host-outline), 2px -2px 0 var(--host-outline),
                 -2px 2px 0 var(--host-outline), 2px 2px 0 var(--host-outline);
  }
  .hosts .present {
    font-family: "Open Sans", sans-serif;
    font-weight: 600;
    color: var(--white);
    font-size: 24px;
    line-height: 40px;
    text-shadow: 0 1px 3px rgba(0,0,0,0.6);
  }
  .event-title {
    position: absolute;
    top: 216px;
    left: 0;
    width: 100%;
    text-align: center;
    font-family: "Black Ops One", sans-serif;
    color: var(--title-green);
    font-size: 52px;
    letter-spacing: 1px;
    line-height: 64px;
  }
  .tagline {
    position: absolute;
    top: 282px;
    left: 0;
    width: 100%;
    text-align: center;
    font-family: "Dancing Script", cursive;
    color: var(--script-dark);
    font-size: 34px;
    line-height: 48px;
  }
  .event-year {
    position: absolute;
    top: 326px;
    left: 0;
    width: 100%;
    text-align: center;
    font-family: "Black Ops One", sans-serif;
    color: var(--title-green);
    font-size: 74px;
    line-height: 84px;
  }
  .date-badge {
    position: absolute;
    left: 548px;
    top: 340px;
    width: 256px;
    height: 220px;
    border-radius: 50%;
    background: var(--badge-orange);
    border: 4px solid var(--badge-ring);
    display: flex;
    flex-direction: column;
    justify-content: center;
    align-items: center;
    font-family: "PT Serif", serif;
    font-weight: 700;
    color: var(--badge-text);
    font-size: 31px;
    line-height: 40px;
    text-align: center;
    white-space: nowrap;
    transform: rotate(-12deg);
  }
  .venue {
    position: absolute;
    top: 628px;
    left: 500px;
    width: 350px;
    text-align: center;
    font-family: "Open Sans", sans-serif;
    font-style: normal;
    font-weight: 600;
    color: var(--address-ink);
    font-size: 21px;
    line-height: 35px;
  }
  .venue .price {
    margin-top: 12px;
    font-weight: 700;
    color: var(--price-red);
    font-size: 28px;
    line-height: 36px;
  }
  .partner {
    position: absolute;
    bottom: 24px;
    left: 0;
    width: 100%;
    text-align: center;
    font-family: "Open Sans", sans-serif;
    font-style: italic;
    font-weight: 600;
    color: var(--white);
    font-size: 29px;
    line-height: 44px;
    text-shadow: 0 1px 4px rgba(0,0,0,0.7);
  }
</style>
</head>
<body>
  <main class="flyer">
    <div class="scene" role="img" aria-label="Cloudy savanna sunset sky with palm tree silhouettes on the horizon"></div>
    <div class="portrait" role="img" aria-label="Photograph of an African woman in a patterned head wrap, bead necklaces and orange draped fabric, holding a wooden bowl"></div>

    <header class="hosts">
      <p>Salon Maribo Hair</p>
      <p>&amp;</p>
      <p>Epicerie exotique Tollane</p>
      <p class="present">present</p>
    </header>

    <h1 class="event-title">CELEBRATING KOLIMBA</h1>
    <p class="tagline">Black is Beautiful</p>
    <p class="event-year">2015</p>

    <div class="date-badge">
      <span>20 juin</span>
      <span>à partir de 20h</span>
    </div>

    <address class="venue">
      Hotel Brimont Lodge<br>
      27, rue des Glacinettes 01210<br>
      Ferney Voltaire
      <p class="price">35€ (repas inclus)</p>
    </address>

    <footer class="partner">
      <p>Avec la participation de l'association</p>
      <p>Aiguilles Solidaires</p>
    </footer>
  </main>
</body>
</html>
```